I need a book jacket cover for my historical fiction novel, Lanterns of Ash. I have a picture for the front cover, the two gold crowns described in the book. I also have a picture for the back cover, a gilded skull cap wine vessel with its box and bottle of wine. The book is about Scythians from 2,000 years ago regrouping in the present to import heroin through Virginia Beach and the Outer Banks.

Font styles to use
Serif

Requirements
Must have
• Leave space on back cover for bar code.
• AUTHOR: Morris Dale Penwick, MD
• Query short edition on back cover or jacket flap first 4 paragraphs describing the book.
• Same document paragraph describing Dr Penwick starting with, "For the past 40 years..."

```html
<!DOCTYPE html>
<html lang="en">
<head>
<meta charset="utf-8">
<title>Lanterns of Ash — Book Jacket</title>
<link rel="stylesheet" href="https://fonts.googleapis.com/css2?family=Cormorant+Garamond:ital,wght@0,500;1,500&family=Cinzel:wght@400&family=Tinos&display=swap">
<style>
  :root{
    --page:#ffffff;
    --ink-black:#000000;
    --back-top:#0c0605;
    --back-mid:#3a1612;
    --back-low:#6b2a22;
    --gold:#d8b66c;
    --gold-bright:#ebc55d;
    --gold-deep:#8a6722;
    --bio:#f1ece2;
    --caption:#f4f1ea;
    --spot:#2b2b2b;
  }
  *{margin:0;padding:0;box-sizing:border-box}
  html,body{width:1200px;height:838px;overflow:hidden;background:var(--page)}
  .jacket{position:absolute;left:40px;top:35px;width:1116px;height:709px;background:var(--ink-black);overflow:hidden}

  /* back cover */
  .back-cover{position:absolute;left:0;top:0;width:536px;height:709px;
    background:linear-gradient(180deg,var(--back-top) 0%,var(--back-top) 30%,var(--back-mid) 55%,var(--back-low) 78%,var(--back-mid) 100%)}
  .still-life{position:absolute;left:20px;top:317px;width:500px;height:330px;
    background:radial-gradient(ellipse at 40% 60%,rgba(190,150,80,.35),rgba(0,0,0,0) 60%),
               linear-gradient(180deg,rgba(20,8,8,0),rgba(10,5,5,.35))}
  .blurb{position:absolute;left:45px;top:58px;width:460px;font-family:"Tinos",serif;font-size:11.2px;line-height:13.7px;color:var(--gold)}
  .blurb p{margin-bottom:13.7px}
  .about-title{position:absolute;left:0;width:536px;top:278px;text-align:center;font-family:"Tinos",serif;font-weight:400;font-size:12px;color:var(--gold-bright)}
  .bio{position:absolute;left:46px;top:291px;width:456px;font-family:"Tinos",serif;font-size:10.6px;line-height:12.8px;letter-spacing:.15px;color:var(--bio)}
  .caption{position:absolute;left:22px;top:646px;font-family:"Tinos",serif;font-size:8.4px;line-height:14px;color:var(--caption)}

  /* spine */
  .spine{position:absolute;left:536px;top:0;width:44px;height:709px;background:var(--ink-black)}
  .spine-title,.spine-author{position:absolute;left:50%;transform-origin:0 0;transform:rotate(90deg);white-space:nowrap;color:var(--gold)}
  .spine-title{top:59px;margin-left:14px;font-family:"Cormorant Garamond",serif;font-size:27px}
  .spine-title em{font-style:italic}
  .spine-author{top:419px;margin-left:8px;font-family:"Cinzel",serif;font-size:15px;letter-spacing:1.5px}

  /* front cover */
  .front-cover{position:absolute;left:580px;top:0;width:536px;height:709px;
    background:radial-gradient(ellipse 60% 35% at 50% 66%,var(--spot),var(--ink-black) 100%)}
  .rider-emblem{position:absolute;left:228px;top:41px;width:72px;height:60px;
    background:radial-gradient(ellipse,var(--gold),var(--gold-deep) 60%,rgba(0,0,0,0) 72%)}
  .title{position:absolute;left:0;top:96px;width:536px;text-align:center;font-family:"Cormorant Garamond",serif;font-weight:500;
    background:linear-gradient(180deg,#f2d98c 0%,#c9a04a 50%,#8a6722 100%);-webkit-background-clip:text;background-clip:text;color:transparent}
  .title-line{display:block}
  .title-main{font-size:92px;line-height:1}
  .title-of{font-size:78px;font-style:italic;line-height:1;margin-top:-6px}
  .title-last{font-size:104px;line-height:1;margin-top:-8px}
  .crowns-photo{position:absolute;left:32px;top:393px;width:468px;height:190px;
    background:radial-gradient(ellipse 50% 45% at 50% 50%,#b88d3a,#6b4a18 55%,rgba(0,0,0,0) 80%)}
  .author{position:absolute;left:0;width:536px;top:628px;text-align:center;font-family:"Cinzel",serif;font-size:27px;letter-spacing:1px;color:var(--gold-bright)}
</style>
</head>
<body>
<div class="jacket">
  <section class="back-cover">
    <div class="still-life" role="img" aria-label="Still life of a gold Scythian plaque with a horse, a gilded bowl on a wooden stand in an open box, and a bottle of red wine"></div>
    <div class="blurb">
      <p>Prominent politicians, bankers, industrialists, businessmen and lawyers are found brutally murdered. They are scalped, their skullcaps removed and their hands skinned. At the same time new ultra pure heroin laced with Fentanyl is showing up on the streets.</p>
      <p>Who could be behind these heinous acts? Are the murders and the new heroin connected?</p>
      <p>Troubled by these events the federal government creates an ultra secret task force to find out and destroy those responsible. The two protagonists, former Strike Unit Nine members, are pulled out of retirement to lead the team. The Harbor Point Naval Station in Virginia Beach is the perfect location to headquarter the team and to unravel the mystery.</p>
      <p>The Lanterns of Ash brings Hampton Roads into focus from colonial times to the present day. Its huge military presence puts it in the forefront in this new war of terror. Most of the action takes place in Virginia Beach, the most populous city in Virginia and a growing tourist area.</p>
    </div>
    <h2 class="about-title">About the Author</h2>
    <div class="bio">
      Dr Penwick has been in the private practice of psychiatry in Virginia Beach for the past 40 years.<br>
      He is the author of the internationally acclaimed book "Fear and the Racing Heart, A Reader's Guide."<br>
      He has had numerous scientific articles and letters to the editor published in scientific journals and newspapers including the "Tidewater Ledger." He has lectured extensively about psychiatry.<br>
      He is tied to the Earth and has written and produced a CD about man's destruction of it along with accompanying t-shirts.<br>
      He is an avid photographer, bonsai artist, landscape artist and cook.<br>
      He and his wife of 47 years are world travelers and have two daughters and two grandchildren.
    </div>
    <p class="caption">The Scythian crowns and plaque are real, circa 200 BCE - 200 CE.<br>As the creators of the first Silk Road the Scythians became wealthy - coveting gold above all else.</p>
  </section>

  <section class="spine">
    <span class="spine-title">Lanterns <em>of</em> Ash</span>
    <span class="spine-author">MORRIS DALE PENWICK, MD</span>
  </section>

  <section class="front-cover">
    <div class="rider-emblem" role="img" aria-label="Small gold figure of a horseman"></div>
    <h1 class="title">
      <span class="title-line title-main">Lanterns</span>
      <span class="title-line title-of">of</span>
      <span class="title-line title-last">Ash</span>
    </h1>
    <div class="crowns-photo" role="img" aria-label="Two ancient gold leaf crowns set with garnets on a dark surface"></div>
    <p class="author">MORRIS DALE PENWICK, MD</p>
  </section>
</div>
</body>
</html>
```